Plumbing Company After Business Card

Business card for a plumbing business that offers a variety of plumbing services including maintenance, domestic and commercial plumbing. My main focus is to offer high quality professional service. A logo on the card would be ideal. Any other questions feel free to email. Cheers

Looking for something modern and upmarket with preferably a matte black background

Business name is Crestline Plumbing and Gas

Industry/Entity Type

Plumbing

Contact Information for Business Card

Crestline Plumbing and Gas
Marcus Thorvale
0472519306
14 Karrabee Drive, Fernhill 3561
crestlineplumbing@mailbay.com.au
ABN 64 915 207 338

Font styles to use
Sans Serif

Colors
1b1b1b
ffffff
3377b5

Requirements
Must have
• Domestic
• Commercial
• Maintenance

```html
<!DOCTYPE html>
<html lang="en">
<head>
<meta charset="utf-8">
<title>Crestline Plumbing and Gas – Business Card</title>
<link href="https://fonts.googleapis.com/css2?family=Arimo:wght@400;700&display=swap" rel="stylesheet">
<style>
  :root {
    --page: #ffffff;
    --brand-blue: #2e77b6;
    --card-black: #060606;
    --ink-light: #ffffff;
  }
  html, body {
    margin: 0;
    padding: 0;
    width: 1200px;
    height: 1200px;
    overflow: hidden;
    background: var(--page);
    font-family: "Arimo", Arial, sans-serif;
    color: var(--ink-light);
  }
  p, h1, h2 { margin: 0; }
  .canvas {
    position: relative;
    width: 1200px;
    height: 1200px;
  }
  .card {
    position: absolute;
    left: 277px;
    width: 640px;
    height: 429px;
    overflow: hidden;
  }
  .card--front { top: 40px; background: var(--brand-blue); }
  .card--back  { top: 559px; background: var(--card-black); }

  .brand-name {
    position: absolute;
    font-weight: 400;
    letter-spacing: 0.02em;
    text-transform: uppercase;
    line-height: 1;
    white-space: nowrap;
  }
  .brand-tagline {
    position: absolute;
    font-weight: 400;
    line-height: 1;
    white-space: nowrap;
  }
  .card--front .brand-name { left: 96px; top: 104px; font-size: 84px; }
  .card--front .brand-tagline { left: 99px; top: 238px; font-size: 37px; }

  .front-contact {
    position: absolute;
    top: 333px;
    font-size: 19px;
    line-height: 1;
    white-space: nowrap;
  }
  .front-contact--name { left: 145px; }
  .front-contact--phone { left: 376px; }
  strong { font-weight: 700; }

  .card--back .brand-name { left: 349px; top: 92px; font-size: 40px; }
  .card--back .brand-tagline { left: 349px; top: 154px; font-size: 19px; }

  .contact-block {
    position: absolute;
    left: 56px;
    top: 130px;
    font-size: 19px;
    line-height: 24px;
    white-space: nowrap;
  }
  .contact-block .contact-name { margin-bottom: 24px; }

  .services-band {
    position: absolute;
    left: 0;
    top: 0;
    width: 640px;
    height: 429px;
  }
  .services-title {
    position: absolute;
    left: 0;
    width: 640px;
    top: 323px;
    text-align: center;
    font-size: 19px;
    line-height: 1;
  }
  .service {
    position: absolute;
    top: 356px;
    font-size: 19px;
    line-height: 1;
    white-space: nowrap;
  }
  .service--maintenance { left: 56px; }
  .service--commercial { left: 262px; }
  .service--domestic { left: 499px; }
</style>
</head>
<body>
<main class="canvas">

  <section class="card card--front" aria-label="Business card front">
    <h1 class="brand-name">Crestline</h1>
    <p class="brand-tagline">Plumbing and Gas</p>
    <p class="front-contact front-contact--name"><strong>Marcus</strong> Thorvale</p>
    <p class="front-contact front-contact--phone">Call: <strong>0472519306</strong></p>
  </section>

  <section class="card card--back" aria-label="Business card back">
    <svg class="services-band" viewBox="0 0 640 429" aria-hidden="true">
      <path d="M0 341 Q320 289 640 337 L640 429 L0 429 Z" fill="var(--brand-blue)"/>
      <path d="M0 341 Q320 289 640 337" fill="none" stroke="var(--ink-light)" stroke-width="1"/>
    </svg>

    <h2 class="brand-name">Crestline</h2>
    <p class="brand-tagline">Plumbing and Gas</p>

    <div class="contact-block">
      <p class="contact-name"><strong>Marcus</strong> Thorvale</p>
      <p>Call: <strong>0472519306</strong></p>
      <p>14 Karrabee Drive, Fernhill 3561</p>
      <p>ABN 64 915 207 338</p>
      <p>crestlineplumbing@mailbay.com.au</p>
    </div>

    <p class="services-title">Plumbing services:</p>
    <p class="service service--maintenance">Maintenance</p>
    <p class="service service--commercial">Commercial</p>
    <p class="service service--domestic">Domestic</p>
  </section>

</main>
</body>
</html>
```